Web Site Design

We need to design the whole web site for our small start up. We sell hospitality and culinary art internships abroad. I did my own design with WIX which is horrible meanwhile I started with my business. You can see it www.brightvoyage-intern.example I will need you to create a new and attractive web site and to leave it working on wix. The internship destinations are United Arab Emirates, Thailand, China, Spain, Brazil and maybe leave a couple of pages for future destinations.You could also get other ideas of other sites that do internships.

Target Market(s)

Students and recent graduates of hospitality and culinary art majors

Industry/Entity Type

Education

Number of Pages Required

5+ page

Requirements
Must have
• Addittional to our program destinations, or to the pages in the current site. The website must contain a page for Universities or Hotels who require our service

```html
<!DOCTYPE html>
<html lang="en">
<head>
<meta charset="utf-8">
<title>Bright Voyage – Hospitality Internships</title>
<link href="https://fonts.googleapis.com/css2?family=Open+Sans:ital,wght@0,400;0,600;0,700;1,400;1,700&family=Zilla+Slab:wght@400;500;600;700&display=swap" rel="stylesheet">
<style>
:root{
  --teal:#2b8c8e;
  --teal-dark:#23777a;
  --black:#050505;
  --ink:#222;
  --muted:#444;
  --light:#e9e9e9;
  --white:#fff;
  --num:#e6e6e6;
}
*{margin:0;padding:0;box-sizing:border-box}
html,body{width:1200px;height:2195px;overflow:hidden;background:var(--white)}
body{position:relative;font-family:"Open Sans",Arial,sans-serif;color:var(--ink)}
.abs{position:absolute}
.slab{font-family:"Zilla Slab",Georgia,serif}
.btn{position:absolute;background:var(--teal);color:var(--white);font-family:"Zilla Slab",Georgia,serif;font-weight:600;font-size:14px;display:flex;align-items:center;justify-content:center}

/* header */
.site-header{left:0;top:0;width:1200px;height:130px;background:var(--black);color:var(--white)}
.topbar{right:128px;top:12px;display:flex;gap:38px;font-size:10px;align-items:center}
.topbar span{display:flex;align-items:center;gap:7px}
.brand{left:132px;top:54px;width:100px;text-align:center;font-size:15px;line-height:15px;letter-spacing:.5px}
.brand i{display:block;width:22px;height:22px;border:2px solid var(--white);border-radius:50%;margin:0 auto 6px}
.nav{top:70px;left:0;width:1200px;font-size:14px}
.nav a{position:absolute;color:var(--white);text-decoration:none}
.nav-mark{left:507px;top:100px}

/* hero */
.hero{left:0;top:130px;width:1200px;height:515px;background:linear-gradient(180deg,#2e3f5a 0%,#4a4a52 45%,#3b2f2b 100%)}
.inquiry{left:136px;top:215px;width:350px;height:331px;background:rgba(235,235,235,.93);padding:0}
.inquiry h2{position:absolute;left:24px;top:16px;width:300px;color:var(--teal);font-family:"Zilla Slab",Georgia,serif;font-weight:600;font-size:22px;line-height:24px}
.inquiry p{position:absolute;left:24px;top:80px;width:290px;font-size:11.5px;line-height:15px;color:#333}
.field{position:absolute;border:1.5px solid var(--teal);font-size:9px;font-style:italic;color:#555;padding:5px 12px}
.socials{position:absolute;display:flex;gap:4px}
.socials i{width:20px;height:20px;border-radius:50%;background:var(--black);display:block}
.hero-copy{left:604px;top:272px;width:470px;color:var(--white)}
.hero-copy h1{font-family:"Zilla Slab",Georgia,serif;font-weight:700;font-size:36px;line-height:38px}
.hero-copy p{font-size:12px;line-height:16px;margin-top:10px}

/* sections */
.section-title{left:0;width:1200px;text-align:center;font-family:"Zilla Slab",Georgia,serif;font-size:28px;color:var(--teal)}
.divider{left:576px;width:48px;height:12px}
.section-lead{left:340px;width:520px;text-align:center;font-size:12px;line-height:15px;color:#333}
.card{position:absolute;width:194px;height:166px;box-shadow:0 3px 6px rgba(0,0,0,.25)}
.card-label{position:absolute;background:rgba(30,20,15,.82);color:var(--white);text-align:center}
.shelf{left:220px;top:995px;width:760px;height:14px;border-radius:50%;box-shadow:0 6px 8px -4px rgba(0,0,0,.35)}

.step-num{position:absolute;font-size:58px;color:var(--num);font-weight:300;line-height:1}
.step-label{position:absolute;font-family:"Zilla Slab",Georgia,serif;font-size:18px;color:var(--ink)}
.step-icon{position:absolute;width:66px;height:66px;border-radius:50%;background:var(--teal);top:1218px}

.universities{left:0;top:1425px;width:1200px;height:423px;background:linear-gradient(180deg,#4a5565 0%,#2d3440 60%,#1f2329 100%)}

.office-h{position:absolute;font-family:"Zilla Slab",Georgia,serif;font-weight:700;font-size:14px;color:var(--teal)}
.office-p{position:absolute;font-size:13px;color:#333}
.contact-line{position:absolute;left:135px;display:flex;align-items:center;gap:14px;font-size:12px;color:#333}

.site-footer{left:0;top:2145px;width:1200px;height:50px;background:var(--black);color:var(--white)}
</style>
</head>
<body>

<header class="abs site-header">
  <div class="abs topbar">
    <span><svg width="14" height="10" viewBox="0 0 14 10"><rect x="0.5" y="0.5" width="13" height="9" fill="none" stroke="#fff"/><path d="M0.5 0.5 L7 6 L13.5 0.5" fill="none" stroke="#fff"/></svg>info@larkfieldcapital.example</span>
    <span><svg width="12" height="12" viewBox="0 0 24 24"><path fill="#fff" d="M6.6 10.8a15.1 15.1 0 0 0 6.6 6.6l2.2-2.2a1 1 0 0 1 1-.25 11.4 11.4 0 0 0 3.6.57 1 1 0 0 1 1 1V20a1 1 0 0 1-1 1A17 17 0 0 1 3 4a1 1 0 0 1 1-1h3.5a1 1 0 0 1 1 1c0 1.25.2 2.45.57 3.57a1 1 0 0 1-.25 1z"/></svg>+99 0100 2200 3</span>
  </div>
  <div class="abs brand"><i></i>BRIGHT<br>VOYAGE</div>
  <nav class="abs nav">
    <a style="left:515px">Home</a>
    <a style="left:606px">Designations</a>
    <a style="left:749px">Process</a>
    <a style="left:867px">Universities</a>
    <a style="left:998px">Contact Us</a>
  </nav>
  <svg class="abs nav-mark" width="62" height="8" viewBox="0 0 62 8"><line x1="0" y1="4" x2="22" y2="4" stroke="#fff"/><circle cx="31" cy="4" r="3" fill="none" stroke="#fff"/><line x1="40" y1="4" x2="62" y2="4" stroke="#fff"/></svg>
</header>

<section class="abs hero" role="img" aria-label="Photo of a red-brick gothic university hall under a cloudy blue sky, framed by trees"></section>

<form class="abs inquiry">
  <h2>Hospitality internships are our specialty!</h2>
  <p>Take your paid internship in one of our top international five-star hotels</p>
  <div class="field" style="left:24px;top:133px;width:138px;height:29px">Name</div>
  <div class="field" style="left:186px;top:133px;width:138px;height:29px">Phone Number</div>
  <div class="field" style="left:24px;top:173px;width:300px;height:29px">Email</div>
  <div class="field" style="left:24px;top:213px;width:300px;height:52px">Message</div>
  <div class="socials" style="left:24px;top:279px"><i></i><i></i><i></i><i></i><i></i></div>
  <div class="btn" style="left:219px;top:278px;width:105px;height:33px">Send</div>
</form>

<div class="abs hero-copy">
  <h1>Hospitality Internships<br>are Available</h1>
  <p>Lorem ipsum dolor sit amet, consectetur adipi sicing elit, sed do eiusmod tempor incididunt ut labore et dolore magna aliquauis aute irure dolor. Nemo enim ipsam voluptatem quia voluptas sit aspernatur aut odit aut fugit, sed quia conseq uuntur magni dolores eos qui ratione voluptatem sequi nesciunt.</p>
</div>
<div class="btn" style="left:604px;top:445px;width:106px;height:32px">Read More</div>

<!-- Designations -->
<h2 class="abs section-title" style="top:672px">Designations</h2>
<svg class="abs divider" style="top:719px" viewBox="0 0 48 12"><line x1="0" y1="6" x2="16" y2="6" stroke="#aaa"/><circle cx="24" cy="6" r="3" fill="none" stroke="#aaa"/><line x1="32" y1="6" x2="48" y2="6" stroke="#aaa"/></svg>
<p class="abs section-lead" style="top:746px">Lorem ipsum dolor sit amet, consectetur adipi sicing elit, sed do eiusmod tempor incididunt ut labore et.doloe magna aliquauis aute irure dolor.</p>

<div class="card" style="left:178px;top:796px;background:linear-gradient(160deg,#c0683a,#6b2c1c)" role="img" aria-label="Photo of a traditional Chinese temple gate"></div>
<div class="card-label" style="left:200px;top:816px;width:150px;height:128px">
  <div class="slab" style="font-size:22px;font-weight:600;margin-top:18px">China</div>
</div>
<div class="btn" style="left:221px;top:888px;width:104px;height:32px">View Info</div>
<div class="card" style="left:400px;top:796px;background:linear-gradient(180deg,#d99a66,#7a5a48 60%,#2c2a30)" role="img" aria-label="Photo of a harbour opera house at sunset"></div>
<div class="card" style="left:620px;top:796px;background:linear-gradient(180deg,#f3b260,#c98a55 55%,#6d5448)" role="img" aria-label="Photo of a sunlit city skyline"></div>
<div class="card" style="left:840px;top:796px;background:linear-gradient(180deg,#c77a42,#8a4a2c 60%,#3a2219)" role="img" aria-label="Photo of a glass pyramid lit at dusk"></div>
<div class="abs shelf"></div>

<!-- Process -->
<h2 class="abs section-title" style="top:1046px">Process</h2>
<svg class="abs divider" style="top:1092px" viewBox="0 0 48 12"><line x1="0" y1="6" x2="16" y2="6" stroke="#aaa"/><circle cx="24" cy="6" r="3" fill="none" stroke="#aaa"/><line x1="32" y1="6" x2="48" y2="6" stroke="#aaa"/></svg>
<p class="abs section-lead" style="top:1111px">Lorem ipsum dolor sit amet, consectetur adipi sicing elit, sed do eiusmod tempor incididunt ut labore et.doloe magna aliquauis aute irure dolor.</p>

<svg class="abs" style="left:200px;top:1249px" width="808" height="4"><line x1="0" y1="2" x2="808" y2="2" stroke="var(--teal)" stroke-width="3" stroke-dasharray="12 6"/></svg>

<div class="step-num" style="left:265px;top:1152px">1</div><div class="step-label" style="left:293px;top:1180px">Apply</div>
<div class="step-num" style="left:364px;top:1272px">2</div><div class="step-label" style="left:408px;top:1298px">Deposit</div>
<div class="step-num" style="left:481px;top:1154px">3</div><div class="step-label" style="left:519px;top:1184px">Interview</div>
<div class="step-num" style="left:598px;top:1268px">4</div><div class="step-label" style="left:641px;top:1294px">Placement</div>
<div class="step-num" style="left:726px;top:1154px">5</div><div class="step-label" style="left:761px;top:1184px">Payment</div>
<div class="step-num" style="left:844px;top:1272px">6</div><div class="step-label" style="left:895px;top:1298px">Visa</div>

<svg class="step-icon" style="left:285px" viewBox="0 0 66 66"><circle cx="33" cy="33" r="33" fill="var(--teal)"/><rect x="23" y="20" width="18" height="24" fill="none" stroke="#fff" stroke-width="2"/><line x1="27" y1="27" x2="37" y2="27" stroke="#fff" stroke-width="2"/><line x1="27" y1="32" x2="37" y2="32" stroke="#fff" stroke-width="2"/><line x1="27" y1="37" x2="34" y2="37" stroke="#fff" stroke-width="2"/><line x1="45" y1="22" x2="45" y2="42" stroke="#fff" stroke-width="2"/></svg>
<svg class="step-icon" style="left:407px" viewBox="0 0 66 66"><circle cx="33" cy="33" r="33" fill="var(--teal)"/><rect x="19" y="23" width="28" height="20" rx="2" fill="none" stroke="#fff" stroke-width="2"/><rect x="38" y="29" width="11" height="8" fill="none" stroke="#fff" stroke-width="2"/></svg>
<svg class="step-icon" style="left:527px" viewBox="0 0 66 66"><circle cx="33" cy="33" r="33" fill="var(--teal)"/><circle cx="33" cy="28" r="6" fill="none" stroke="#fff" stroke-width="2"/><path d="M21 45c2-7 22-7 24 0" fill="none" stroke="#fff" stroke-width="2"/><rect x="19" y="18" width="28" height="29" fill="none" stroke="#fff" stroke-width="2"/></svg>
<svg class="step-icon" style="left:652px" viewBox="0 0 66 66"><circle cx="33" cy="33" r="33" fill="var(--teal)"/><path d="M33 46s-9-10-9-16a9 9 0 0 1 18 0c0 6-9 16-9 16z" fill="none" stroke="#fff" stroke-width="2"/><circle cx="33" cy="30" r="3" fill="#fff"/><ellipse cx="33" cy="47" rx="11" ry="3" fill="none" stroke="#fff" stroke-width="1.5"/></svg>
<svg class="step-icon" style="left:765px" viewBox="0 0 66 66"><circle cx="33" cy="33" r="33" fill="var(--teal)"/><circle cx="37" cy="24" r="6" fill="none" stroke="#fff" stroke-width="2"/><path d="M18 40l8-5h9l-4 4h8l10-6" fill="none" stroke="#fff" stroke-width="2"/><path d="M18 46l8-3h12l12-8" fill="none" stroke="#fff" stroke-width="2"/></svg>
<svg class="step-icon" style="left:877px" viewBox="0 0 66 66"><circle cx="33" cy="33" r="33" fill="var(--teal)"/><rect x="22" y="17" width="22" height="32" rx="2" fill="none" stroke="#fff" stroke-width="2"/><circle cx="33" cy="29" r="6" fill="none" stroke="#fff" stroke-width="2"/><line x1="27" y1="41" x2="39" y2="41" stroke="#fff" stroke-width="2"/></svg>

<div class="btn" style="left:552px;top:1354px;width:103px;height:32px">View Info</div>

<!-- Universities -->
<section class="abs universities" role="img" aria-label="Photo of graduates throwing caps into the air"></section>
<h2 class="abs section-title" style="top:1458px;color:var(--white)">Universities</h2>
<svg class="abs divider" style="top:1498px" viewBox="0 0 48 12"><line x1="0" y1="6" x2="16" y2="6" stroke="#fff"/><circle cx="24" cy="6" r="3" fill="none" stroke="#fff"/><line x1="32" y1="6" x2="48" y2="6" stroke="#fff"/></svg>
<p class="abs section-lead" style="top:1521px;color:var(--white)">Lorem ipsum dolor sit amet, consectetur adipi sicing elit, sed do eiusmod tempor incididunt ut labore et.doloe magna aliquauis aute irure dolor.</p>

<div class="card" style="left:178px;top:1573px;background:linear-gradient(180deg,#8aa3c2,#7a5a3a 60%,#4a6a2a)" role="img" aria-label="Photo of a traditional university gate"></div>
<div class="card-label" style="left:194px;top:1587px;width:160px;height:152px;background:rgba(15,15,15,.85)">
  <div class="slab" style="font-size:17px;font-weight:700;line-height:16px;margin-top:24px">Eastfield<br>University</div>
  <div style="font-size:7px;font-style:italic;margin-top:5px">Beijing , China</div>
</div>
<div class="btn" style="left:221px;top:1669px;width:104px;height:32px">View Info</div>
<div class="card" style="left:397px;top:1573px;background:linear-gradient(180deg,#6f9fd8,#cfc6b4 55%,#4f8a3a)" role="img" aria-label="Photo of a classical palace building with flags"></div>
<div class="card" style="left:620px;top:1573px;background:linear-gradient(180deg,#6aa3dc,#a4553a 50%,#6a3a2a)" role="img" aria-label="Photo of a red-brick castle university"></div>
<div class="card" style="left:840px;top:1573px;background:linear-gradient(180deg,#5a8fd0,#d9d4cc 50%,#4f8e3a)" role="img" aria-label="Photo of a domed campus building behind white columns"></div>

<div class="btn" style="left:550px;top:1777px;width:104px;height:33px">Read More</div>

<!-- Contact -->
<h2 class="abs section-title" style="top:1879px">Contact Us</h2>
<svg class="abs divider" style="top:1917px" viewBox="0 0 48 12"><line x1="0" y1="6" x2="16" y2="6" stroke="#aaa"/><circle cx="24" cy="6" r="3" fill="none" stroke="#aaa"/><line x1="32" y1="6" x2="48" y2="6" stroke="#aaa"/></svg>

<p class="abs" style="left:135px;top:1941px;width:455px;font-size:12px;line-height:16px;color:#333">Lorem ipsum dolor sit amet, consectetur adipiscing elit, sed do eiusmod tempor incididunt ut labore et dolore magna aliqua. Ut enim ad minim veniam, quis nostrud exercitation ullamco laboris nisi ut aliquip ex ea commodo conse-quat. Duis aute irure dolor in reprehenderit in voluptate velit esse cillum dolore eu fugiat nulla pariatur.</p>

<div class="contact-line" style="top:2047px"><svg width="14" height="16" viewBox="0 0 14 16"><path d="M7 15S1 9 1 6a6 6 0 0 1 12 0c0 3-6 9-6 9z" fill="#111"/><circle cx="7" cy="6" r="2" fill="#fff"/></svg>Lorem Ipsum 123 , 890</div>
<div class="contact-line" style="top:2069px"><svg width="14" height="14" viewBox="0 0 24 24"><path fill="#111" d="M6.6 10.8a15.1 15.1 0 0 0 6.6 6.6l2.2-2.2a1 1 0 0 1 1-.25 11.4 11.4 0 0 0 3.6.57 1 1 0 0 1 1 1V20a1 1 0 0 1-1 1A17 17 0 0 1 3 4a1 1 0 0 1 1-1h3.5a1 1 0 0 1 1 1c0 1.25.2 2.45.57 3.57a1 1 0 0 1-.25 1z"/></svg>+54 000 111</div>
<div class="contact-line" style="top:2091px"><svg width="15" height="11" viewBox="0 0 15 11"><rect x="0" y="0" width="15" height="11" fill="#111"/><path d="M0.5 0.5L7.5 6L14.5 0.5" fill="none" stroke="#fff"/></svg>info@brightvoyage-intern.example</div>

<h3 class="abs slab" style="left:642px;top:1940px;font-weight:400;font-size:18px;color:var(--teal)">Our Offices</h3>
<div class="office-h" style="left:642px;top:1978px">Mexico</div>
<div class="office-p" style="left:642px;top:1998px">+52 55 0100 2000</div>
<div class="office-h" style="left:802px;top:1978px">Europe</div>
<div class="office-p" style="left:802px;top:1998px">+33 7 0100 2001</div>
<div class="office-h" style="left:642px;top:2030px">United States</div>
<div class="office-p" style="left:642px;top:2054px">+1 307-555-0142</div>
<div class="office-h" style="left:802px;top:2030px">Australia</div>
<div class="office-p" style="left:802px;top:2054px">+61 402 000 111</div>

<footer class="abs site-footer">
  <p class="abs" style="left:136px;top:18px;font-size:11px;font-style:italic;font-weight:700">Copyright by Larkfield Capital . All Right Reserved © 2018</p>
  <div class="abs" style="left:912px;top:15px;display:flex;gap:19px">
    <i style="display:block;width:17px;height:17px;border-radius:50%;background:var(--white)"></i>
    <i style="display:block;width:17px;height:17px;border-radius:50%;background:var(--white)"></i>
    <i style="display:block;width:17px;height:17px;border-radius:50%;background:var(--white)"></i>
    <i style="display:block;width:17px;height:17px;border-radius:50%;background:var(--white)"></i>
    <i style="display:block;width:17px;height:17px;border-radius:50%;background:var(--white)"></i>
  </div>
</footer>

</body>
</html>
```